Flyer Design For Tech Support Company

We need a flyer design for our company Corvalo Crafted Systems Ltd. I would like this to follow the same theme and styling of: www.corvalosys.co.uk I would also invite you to use any information as found on our site. I would like this to focues primarily on attracting small bussines/start-up new custom; additionaly if there could be a mention of being able to work with private customers also.

Target Market(s)

Start-up, Small Businnes, Private Home.

Industry/Entity Type

It Company

Font styles to use
Sans Serif

Colors
33a6d7

Requirements
Must have
• Follow theme/style of main site.
• Be bold to attract from a distance.
Should not have
• Funny's

```html
<!DOCTYPE html>
<html lang="en">
<head>
<meta charset="utf-8">
<title>Corvalo Crafted Systems Ltd – Tech Support Flyer</title>
<link rel="stylesheet" href="https://fonts.googleapis.com/css2?family=Mulish:ital,wght@0,400;0,800;0,900;1,800&family=Montserrat:wght@700&display=swap">
<style>
  :root {
    --sky: #3fc4ef;
    --band: #4fd0f6;
    --tick: #3fb9ea;
    --ink: #262626;
    --panel: #eceeed;
    --pill: #2b2a26;
    --paper: #ffffff;
    --board-dark: #22272a;
    --board-mid: #3a4140;
  }
  * { box-sizing: border-box; margin: 0; padding: 0; }
  html, body { width: 856px; height: 1200px; overflow: hidden; background: var(--paper); }
  body { font-family: "Mulish", "Helvetica Neue", Arial, sans-serif; color: var(--ink); }

  .flyer { position: relative; width: 856px; height: 1200px; background: var(--paper); }

  .hero {
    position: absolute; left: 0; top: 0; width: 856px; height: 392px;
    background:
      radial-gradient(ellipse 170px 190px at 430px 150px, rgba(185,220,46,.55), transparent 70%),
      radial-gradient(ellipse 140px 120px at 60px 90px, rgba(40,160,60,.5), transparent 70%),
      radial-gradient(ellipse 150px 130px at 800px 110px, rgba(40,100,220,.5), transparent 70%),
      radial-gradient(ellipse 140px 90px at 800px 340px, rgba(230,200,40,.45), transparent 70%),
      linear-gradient(160deg, var(--board-mid), var(--board-dark));
  }
  .hero-band { position: absolute; left: 0; top: 392px; width: 856px; height: 9px; background: var(--band); }

  .headline {
    position: absolute; left: 0; top: 438px; width: 856px;
    text-align: center; color: var(--sky);
    font-weight: 900; font-size: 26.6px; line-height: 30px; letter-spacing: -.3px;
    text-transform: uppercase;
  }

  .services { position: absolute; left: 62px; top: 526px; list-style: none; }
  .services li { height: 30.8px; font-size: 17px; line-height: 24px; padding-left: 18px; position: relative; letter-spacing: -.1px; white-space: nowrap; }
  .tick { position: absolute; left: 0; top: 4px; width: 16px; height: 14px; }

  .brand { position: absolute; left: 620px; top: 616px; width: 190px; text-align: center; }
  .brand-dot { display: block; margin: 0 auto 18px; width: 96px; height: 96px; border-radius: 50%; background: var(--band); }
  .brand-name { color: var(--sky); font-weight: 400; font-size: 20px; line-height: 25px; }

  .extras { position: absolute; left: 0; top: 834px; width: 856px; height: 192px; background: var(--panel); }
  .extras-title {
    position: absolute; left: 0; top: 31px; width: 856px; text-align: center;
    font-weight: 900; font-size: 15.9px; line-height: 19px; text-transform: uppercase; letter-spacing: -.2px;
  }
  .extras-list { position: absolute; top: 76px; list-style: none; }
  .extras-list.left { left: 62px; }
  .extras-list.right { left: 440px; }
  .extras-list li { height: 30.8px; font-size: 17px; line-height: 24px; padding-left: 18px; position: relative; white-space: nowrap; }

  .tagline {
    position: absolute; left: 0; top: 1052px; width: 856px; text-align: center;
    font-style: italic; font-weight: 800; font-size: 25px; letter-spacing: -1.3px; line-height: 34px;
  }

  .call {
    position: absolute; left: 219px; top: 1102px; width: 418px; height: 46px;
    border-radius: 23px; background: var(--pill); color: var(--paper);
    font-family: "Montserrat", Arial, sans-serif; font-weight: 700; font-size: 33px; letter-spacing: 2.4px;
    line-height: 46px; text-align: center;
  }
</style>
</head>
<body>
<main class="flyer">
  <svg width="0" height="0" style="position:absolute">
    <symbol id="tick" viewBox="0 0 16 14"><path d="M1 8 L6 12 L15 1" fill="none" stroke="#3fb9ea" stroke-width="3" stroke-linecap="round" stroke-linejoin="round"/></symbol>
  </svg>

  <div class="hero" role="img" aria-label="Photo from above of people around a chalkboard table drawing a glowing light bulb idea, with coffee cups and notebooks"></div>
  <div class="hero-band"></div>

  <h1 class="headline">We don’t believe in packages. But here are some<br>service examples of what we can do for you:</h1>

  <ul class="services">
    <li><svg class="tick"><use href="#tick"/></svg>PC (Operating Fenwick, OrbixOS or Tarnix) Software Rebuild and Troubleshoot.</li>
    <li><svg class="tick"><use href="#tick"/></svg>PC Hardware Troubleshoot or Upgrade.</li>
    <li><svg class="tick"><use href="#tick"/></svg>Home or Business Network (Wired or Wi-Fi) Installation or Troubleshoot.</li>
    <li><svg class="tick"><use href="#tick"/></svg>Telephone Extension Installation or Troubleshoot.1</li>
    <li><svg class="tick"><use href="#tick"/></svg>Home Automation Installation e.g. Kestrel Remote Thermostat.</li>
    <li><svg class="tick"><use href="#tick"/></svg>Home or Business Backup Solutions.</li>
    <li><svg class="tick"><use href="#tick"/></svg>Home or Business Server Install, Configure or Secure.</li>
    <li><svg class="tick"><use href="#tick"/></svg>Home or Business IT/Tech Consultation Service.</li>
    <li><svg class="tick"><use href="#tick"/></svg>On call Tech Support, let us be your own IT Team.</li>
  </ul>

  <div class="brand">
    <span class="brand-dot"></span>
    <p class="brand-name">Corvalo Crafted<br>Systems Ltd</p>
  </div>

  <section class="extras">
    <h2 class="extras-title">We also offer a “Q-HUB” service to bring your home or business online and open<br>to your friends, family and customers; this can include but is not limited to:</h2>
    <ul class="extras-list left">
      <li><svg class="tick"><use href="#tick"/></svg>Your own domain name (.com or .co.uk)</li>
      <li><svg class="tick"><use href="#tick"/></svg>Your own website – yourowndomain.com</li>
      <li><svg class="tick"><use href="#tick"/></svg>Remote Backup Services</li>
    </ul>
    <ul class="extras-list right">
      <li><svg class="tick"><use href="#tick"/></svg>Online Shop or E-Commerce setup</li>
      <li><svg class="tick"><use href="#tick"/></svg>Private and secure e-mail service,</li>
      <li>tied to your own domain</li>
    </ul>
  </section>

  <p class="tagline">“Providing a cost-effective consultation, design and support service.”</p>

  <p class="call">CALL: 07700 418265</p>
</main>
</body>
</html>
```